Website Redesign Project

Bright Harbour Consulting provides project management and project controls consultancy services to companies in many industry sectors, within Australia and overseas. My company has been developing a business brand through forging strong business relationships within industry. We provide innovative tools, concepts and solutions to management teams to assist them in better plan and managing there project portfolios.
SECTORS OF INDUSTRY WE SERVICE
★Oil & Gas
★Minerals & Metals
★Petrochemical
★Manufacturing
★Building & Construction
★Telecommunications
★Rail
★Civil
OLD WEBSITE
My old website www.brightharbourconsulting.com.au needs a complete overhaul in terms of how the web pages look and feel. I am trying to get away from the grey, washed out look as it is uninviting and dull. My clients commented that my webpage does not reflect who I am as a company or my core values. Think total redesign
DESIGN
I would like a webpage design that is modern and has a corporate image. It must be elegant, classy, and have an overall glossy appearance. I want something exciting that creates some excellent feedback from clients. It needs to have a savvy appearance and an attitude of a market leader. A generic website template cannot be used as I provide a unique service to clients. I do not need a website design that looks like my compeditors, I want something that stands out in the crowd and effectivly markets my bussinesses brand. I want my website to represent quality, so only high resolution images that are clear, sharp and in focus can be used. With this design, throw your standard webpage design concepts out the window, as I want something fresh, innovative, exciting and inviting. The overall design should appear uncluttered as all content needs to be there for a reason, so think functional.
It must be professional and of the highest calibre as my clients expect nothing less. I provide clients with innovative tools, concepts and solutions, so the design needs to be edgy and creative to align with my company’s core business services. The new design must promote the company’s brand and us as a market leader. It must communicate that we service many industry sectors and reflect our company’s creativity, vision, energy and drive.
WEBPAGE WRITTEN CONTENT
I am happy with the written content on each page within my old website. You may arrange the text how you see fit within the new design. On the main page of my old website the text is under scored, I am not a big fan of this. I currently do not like the format the text is in, I am looking for a formatt that is easy to read, looks flattering and pleasing to the eye.
MAIN PAGE DESIGN
The main page design needs to focus on my company as a brand, it must promote that I service many industry sectors. My old webpage had me pigeon holed as only providing services to oil and gas. This is incorrect as I service oil & gas, metals and minerals, Petrochemical, Manufacturing, Building & Construction, Telecommunications, Rail and civil.
WEBPAGE COLUR PREFERENCE
Prefer a white background with plenty of colour
TESTIMONIAL TAB
The testimonial tab on the task bar can be removed as it is no longer required.
FINISHED PRODUCT
The finished product will be uploaded by you to a nominated web hosting account. I will need a copy of all files associated with the design. A copy of the finished product will also be provided in formats that can me imported to Xara Pro Designer as I will update my website in 6 months or so using this tool.
Updates
I have updated the design brief after recieving feedback from several designers
Thanks
Hi All
I have just launched another project called "bright harbour consulting business card redesign project", you are all welcome to join this project.
Thanks
Target Market(s)
★Oil and Gas
★Mining and Resources
★Building and infrastructure
★Petrochemical
★Civil and roads
★Rail
Industry/Entity Type
Industry
Requirements
Must have
- ★Draw you in
★Hold your attention
★Identify company brand
★Highlight skills experience and expertise
★Be a unique design not generic
Should not have
- ★The webpage design should not be old fashioned
★ The design should not be based off a generic design template
★The webpage should not be cluttered; everything needs to be there for a reason.

```html
<!DOCTYPE html>
<html lang="en">
<head>
<meta charset="utf-8">
<title>Bright Harbour Consulting</title>
<link href="https://fonts.googleapis.com/css2?family=Ubuntu:ital,wght@0,400;0,500;0,700;1,400&display=swap" rel="stylesheet">
<style>
:root{
  --ink:#1a1a1a;
  --text:#333333;
  --band:#2b2b2b;
  --red:#c4231f;
  --bullet:#e0191b;
  --blush:#ead3d5;
  --orange:#e2650f;
  --white:#ffffff;
  --fb:#3b5998;
  --rss:#e68a1c;
  --yt:#c3281c;
  --tm:#4a79b3;
}
*{margin:0;padding:0;box-sizing:border-box}
html,body{width:1200px;height:934px;overflow:hidden;background:var(--white)}
body{font-family:"Ubuntu",sans-serif;color:var(--text);position:relative}
.page{position:relative;width:1200px;height:934px;overflow:hidden}

.hero-wash{position:absolute;left:0;top:249px;width:1200px;height:340px;
  background:linear-gradient(180deg,var(--blush) 0%,#f3e4e5 55%,var(--white) 100%)}

.brand{position:absolute;left:151px;top:104px;display:flex;align-items:center;gap:10px}
.brand-mark{width:30px;height:30px;border-radius:50%;background:var(--red)}
.brand-name{font-size:22px;font-weight:700;color:var(--ink);letter-spacing:-.3px}
.brand-tag{position:absolute;left:191px;top:136px;font-size:7px;color:var(--ink)}

.social{position:absolute;top:142px;left:935px;display:flex;gap:12px;list-style:none}
.social li{width:27px;height:27px;border-radius:50%}
.social .s1{background:var(--fb)}.social .s2{background:var(--rss)}
.social .s3{background:var(--yt)}.social .s4{background:var(--tm)}

.nav{position:absolute;left:0;top:188px;width:1200px;height:61px;background:var(--band)}
.nav ul{list-style:none;position:absolute;top:20px;display:flex;gap:25px}
.nav a{color:var(--white);text-decoration:none;font-size:13.5px}
.nav .left{left:150px}
.nav .right{right:126px;gap:29px}

.help{position:absolute;left:937px;top:272px;display:flex;align-items:center;gap:10px}
.help-icon{width:27px;height:27px;border-radius:50%;background:var(--ink);display:flex;align-items:center;justify-content:center}
.help-title{font-size:19px;color:var(--ink);line-height:1}
.help-sub{font-size:7.5px;color:var(--ink)}

.sectors{position:absolute;left:150px;top:330px;display:flex;gap:7px;list-style:none}
.sectors li{width:57px;height:57px;border-radius:50%}
.c1{background:#9c4f24}.c2{background:#7663a3}.c3{background:#1d5f8c}
.c4{background:#6e5a32}.c5{background:#dc2461}.c6{background:#a51d4a}

.services{position:absolute;left:149px;top:428px;width:526px;height:124px;border-radius:12px;overflow:hidden;
  background:linear-gradient(100deg,#6a1212 0%,#8e1a18 38%,#2a2424 60%,#4a3a34 80%,#c45a2a 100%)}
.services h2{position:absolute;left:35px;top:44px;font-size:29px;font-weight:500;color:var(--white)}

.intro{position:absolute;left:738px;top:322px;width:345px}
.intro h1{font-size:26px;font-weight:400;color:var(--ink);margin-bottom:10px;white-space:nowrap;line-height:1.2}
.intro p{font-size:11.8px;line-height:16.6px}

.news{position:absolute;left:736px;top:425px;width:345px}
.news h2{font-size:29px;font-weight:400;color:var(--ink);margin-bottom:12px}
.news-item{display:flex;gap:19px;margin-bottom:22px}
.news-thumb{flex:none;width:97px;height:72px;background:linear-gradient(135deg,#c9a46a,#6b3c2a 45%,#d8c8b0 70%,#8a5a3a)}
.news-date{font-size:11px;font-style:italic;color:var(--ink);margin-bottom:2px}
.news-body{font-size:11.8px;line-height:16.6px}
.all-news{position:absolute;left:975px;top:715px;width:95px;height:33px;border-radius:17px;background:var(--orange);
  color:var(--white);font-size:15.5px;display:flex;align-items:center;justify-content:center;text-decoration:none}

.projects{position:absolute;left:148px;top:585px}
.projects h2{font-size:30px;font-weight:400;color:var(--ink)}
.proj-list{position:absolute;top:50px;list-style:none;font-size:11.8px;line-height:16.6px;white-space:nowrap}
.proj-list li::before{content:"•";color:var(--bullet);margin-right:7px;margin-left:-12px}
.col1{left:14px}.col2{left:162px}.col3{left:388px;top:49px}

.footer{position:absolute;left:0;top:781px;width:1200px;height:153px;background:var(--red);color:var(--white)}
.foot-col{position:absolute;top:33px;list-style:none;font-size:10px;line-height:14.8px}
.foot-col .head{font-weight:500;font-size:10.5px;margin-bottom:1px}
.fc1{left:158px}.fc2{left:273px}.fc3{left:439px}
.copyright{position:absolute;left:738px;top:56px;font-size:10.5px;line-height:14.8px}
</style>
</head>
<body>
<div class="page">
  <div class="hero-wash"></div>

  <div class="brand"><span class="brand-mark"></span><span class="brand-name">Bright Harbour Consulting</span></div>
  <div class="brand-tag">Providing Effective Project Controls and Management Solutions</div>

  <ul class="social" aria-label="Social links">
    <li class="s1"></li><li class="s2"></li><li class="s3"></li><li class="s4"></li>
  </ul>

  <nav class="nav">
    <ul class="left">
      <li><a href="#">About Us</a></li><li><a href="#">Expertise</a></li>
      <li><a href="#">Knowledge</a></li><li><a href="#">Experience</a></li>
    </ul>
    <ul class="right">
      <li><a href="#">Projects</a></li><li><a href="#">Focus</a></li>
      <li><a href="#">Contact</a></li><li><a href="#">Recruitment</a></li>
    </ul>
  </nav>

  <div class="help">
    <span class="help-icon">
      <svg width="15" height="11" viewBox="0 0 15 11"><rect x="0.5" y="0.5" width="14" height="10" rx="1.5" fill="#fff"/><path d="M1 1.5 L7.5 6.5 L14 1.5" fill="none" stroke="#1a1a1a" stroke-width="1.3"/></svg>
    </span>
    <div><div class="help-title">Need Help</div><div class="help-sub">Contact us now</div></div>
  </div>

  <ul class="sectors">
    <li class="c1" role="img" aria-label="Environment sector icon"></li>
    <li class="c2" role="img" aria-label="Manufacturing sector icon"></li>
    <li class="c3" role="img" aria-label="Wind energy sector icon"></li>
    <li class="c4" role="img" aria-label="Electric vehicle sector icon"></li>
    <li class="c5" role="img" aria-label="Energy efficiency sector icon"></li>
    <li class="c6" role="img" aria-label="Fuel sector icon"></li>
  </ul>

  <section class="services" role="img" aria-label="Photo of a mine worker in hard hat and high-visibility gear">
    <h2>Services</h2>
  </section>

  <section class="intro">
    <h1>Bright Harbour Consulting</h1>
    <p>I provide services to companies in the mining and oil and gas sector, to enabling them to plan and manage their construction projects more effectively.</p>
  </section>

  <section class="news">
    <h2>Latest News</h2>
    <article class="news-item">
      <div class="news-thumb" role="img" aria-label="Close-up photo of electronic components"></div>
      <div><div class="news-date">June, 18 2013</div>
        <p class="news-body">I provide services to companies in the mining and oil and gas sector, to enabling them to plan and manage their construction projects more effectively.</p></div>
    </article>
    <article class="news-item">
      <div class="news-thumb" role="img" aria-label="Close-up photo of electronic components"></div>
      <div><div class="news-date">July, 23 2013</div>
        <p class="news-body">I provide services to companies in the mining and oil and gas sector, to enabling them to plan and manage their them to plan and manage their construction projects more effectively. and manage their construction projects more effectively.</p></div>
    </article>
  </section>
  <a class="all-news" href="#">All News</a>

  <section class="projects">
    <h2>Projects</h2>
    <ul class="proj-list col1"><li>Oil &amp; Gas</li><li>Iron Ore</li><li>Coal</li><li>Civil</li><li>Tenders</li><li>Telecomunications</li></ul>
    <ul class="proj-list col2"><li>New Industry</li><li>Petrochemical</li><li>Building And Constructionoil &amp; Gas</li><li>Engineering</li><li>Manufacturing</li><li>Rail</li></ul>
    <ul class="proj-list col3"><li>Oil &amp; Gas</li><li>Iron Ore</li><li>Coal</li><li>Civil</li><li>Tenders</li><li>Telecomunications</li></ul>
  </section>

  <footer class="footer">
    <ul class="foot-col fc1"><li class="head">SOFTWARE</li><li>Advice</li><li>Vision</li><li>Solutions</li><li>Solutions</li><li>Perspective</li></ul>
    <ul class="foot-col fc2"><li class="head">CONTACTS</li><li>Develop and evolve</li><li>Streamlines processes</li><li>Embrace and drive change</li><li>outcomes</li></ul>
    <ul class="foot-col fc3"><li class="head">RESOURCES</li><li>Systems</li><li>Standards</li><li>Procedures</li><li>Process</li></ul>
    <p class="copyright">©Copyright by 2013 Bright Harbour Consulting.<br>All rights reserved</p>
  </footer>
</div>
</body>
</html>
```